New Fun, Positive, energised looking Business Card Needed for High Achiever Coach

I am looking for a two sided full colour business card. I am self employed and have recently re branded my 1-2-1 work re-vitalising high achievers. My target client base for these cards is therefore high achievers - usually aged 40 -55, they are often entrepreneurs, CEO or work in banking and finance and 2/3 are male. I work with them on 90 day or 6 month coaching programs to help them live their success in a healthier, more sustainable and fulfiiled way. They pay for this privately so though they are corporate types the cards need not look 'corporate'. I want to portray the idea of transformation, vitality and re-connecting.
You can get a feel for the look I like on my new website: corinvale.co.uk
I want to use this logo with strapline (Re-Vitalising High Achievers) (I purchased off Logoharbor) and font/ colours (the turquoise and green).
Details to include on the card:
www.corinvale.co.uk
+44 7915 264318
mira@corinvale.co.uk
skype: miracorin
I'd also like to include:
Do you struggle to switch off? Want to be healthier and feel fitter? Want closer relationships? More clarity over the direction you are headed? I can help you do these things using integrated mind-body techniques. Visit corinvale.co.uk TODAY to apply for a FREE Breakthrough session.
BUT if that is too much text for a card I am open to advice/ammendments.
Updates
Thanks for your design - I am considering them. PLease change the wording to :

```html
<!DOCTYPE html>
<html lang="en">
<head>
<meta charset="utf-8">
<title>Mira Corin – Business Card</title>
<link rel="stylesheet" href="https://fonts.googleapis.com/css2?family=Open+Sans:wght@400;600;700&display=swap">
<style>
  :root {
    --turquoise: #0ea8cb;
    --sky: #7fd0ec;
    --leaf: #62bb5e;
    --white: #ffffff;
    --backdrop: #e6e6e6;
  }
  * { box-sizing: border-box; margin: 0; padding: 0; }
  html, body {
    width: 1200px; height: 693px; overflow: hidden;
    background: var(--backdrop);
    font-family: "Open Sans", sans-serif;
  }
  .canvas { position: relative; width: 1200px; height: 693px; }
  .card {
    position: absolute; top: 200px; width: 460px; height: 268px;
    overflow: hidden;
  }
  .card--back { left: 96px; background: var(--turquoise); color: var(--white); text-align: center; }
  .card--front { left: 644px; background: var(--white); }

  .back__mark {
    display: flex; align-items: center; justify-content: center; gap: 8px;
    margin-top: 40px; font-weight: 700; font-size: 16px; color: var(--white);
  }
  .back__mark-dot { width: 12px; height: 12px; border-radius: 50%; background: var(--white); }
  .back__pitch { margin-top: 16px; font-size: 12px; line-height: 16.5px; }
  .back__cta {
    position: absolute; left: 0; right: 0; bottom: 22px;
    font-size: 11.5px; word-spacing: 3px;
  }
  .back__cta strong { font-weight: 700; }

  .front__swoosh { position: absolute; inset: 0; }
  .front__brand {
    position: absolute; left: 20px; top: 92px; width: 190px; text-align: center;
  }
  .front__brand-dot {
    width: 40px; height: 40px; border-radius: 50%; background: var(--leaf);
    margin: 0 auto 14px;
  }
  .front__brand-name { font-weight: 700; font-size: 22px; color: var(--turquoise); }
  .front__strapline { margin-top: 2px; font-size: 10.5px; color: var(--turquoise); }

  .front__details { position: absolute; left: 276px; top: 76px; color: var(--white); }
  .front__name { font-size: 13px; }
  .front__role { font-size: 10.5px; margin-top: 1px; }
  .front__contacts { list-style: none; margin-top: 22px; font-size: 10px; line-height: 15.5px; }
  .front__contacts li { display: flex; align-items: center; gap: 6px; }
  .front__contacts svg { width: 8px; height: 8px; fill: var(--white); }
  .front__web { margin-top: 14px; font-size: 11px; font-weight: 700; }
</style>
</head>
<body>
<main class="canvas">

  <section class="card card--back">
    <div class="back__mark"><span class="back__mark-dot"></span>Mira Corin</div>
    <p class="back__pitch">
      Do you struggle to switch off?<br>
      Want to be healthier and feel fitter?<br>
      Want closer relationships?<br>
      More clarity over the direction you are headed?<br>
      Let me help you reach your goals<br>
      using integrated mind-body techniques.
    </p>
    <p class="back__cta">Visit <strong>corinvale.co.uk</strong> TODAY to apply for a <strong>FREE</strong> Breakthrough session.</p>
  </section>

  <section class="card card--front">
    <svg class="front__swoosh" viewBox="0 0 460 268" preserveAspectRatio="none" aria-hidden="true">
      <path d="M178,0 C252,70 250,200 196,268 L460,268 L460,0 Z" fill="var(--sky)"/>
      <path d="M200,0 C262,72 258,200 206,268 L460,268 L460,0 Z" fill="var(--turquoise)"/>
      <path d="M244,96 C246,170 230,225 196,268" fill="none" stroke="var(--leaf)" stroke-width="4"/>
    </svg>

    <div class="front__brand">
      <div class="front__brand-dot"></div>
      <div class="front__brand-name">Mira Corin</div>
      <div class="front__strapline">Re-Vitalising High Achievers</div>
    </div>

    <div class="front__details">
      <div class="front__name">Mira Corin</div>
      <div class="front__role">President/Revitalising Coach</div>
      <ul class="front__contacts">
        <li><svg viewBox="0 0 10 10"><path d="M2,0 L4,2.5 L3,3.8 C3.8,5.4 4.6,6.2 6.2,7 L7.5,6 L10,8 L8.5,10 C4,9 1,6 0,1.5 Z"/></svg>+44 7915 264318</li>
        <li><svg viewBox="0 0 10 10"><circle cx="5" cy="5" r="5"/></svg>miracorin</li>
        <li><svg viewBox="0 0 10 10"><path d="M0,2 H10 V8 H0 Z M0,2 L5,5.5 L10,2" /></svg>mira@corinvale.co.uk</li>
      </ul>
      <div class="front__web">www.corinvale.co.uk</div>
    </div>
  </section>

</main>
</body>
</html>
```